My new Bible based podcast needs a Podcast Cover Design for Vexora directory

I need a Podcast Cover Design design for my podcast listing in Vexora. The podcast is called Morning Lanterns Over Hills. I would like something cheerful, warm, and fresh because I take a non-traditional approach to explaining how the Bible is relevant to people today. My goal is to get back to the original spirituality of the Bible without all the centuries of added man-made doctrines. It would be great to show a sense of peace and hope, with new possibilities. This is not like a floating corporate logo. I need it to be square and full color/design all the way to the edges.

I have resubmitted this project because I did not understand how to ask for a podcast cover design. If you already submitted for me, I apologize for not knowing how the system works. I did not give the best picture of what I needed.

Target Market(s)

People who want a fresh look at the Bible

Industry/Entity Type

Religious

Logo Text

Morning Lanterns Over Hills

Colors

Designer to choose colors to be used in the design.

Requirements
Must have
• It must be square. The design should fill the space. See screen shot below of podcast cover designs on the Christianity/Spirituality page of Vexora directory so you can see where the podcast cover design needs to fit in and stand out.
• The final design will need to be:
• 3,000 x 3,000 pixels (but readable at 150 x 150)
• 72 dpi
• .jpg or .png format
• rgb color space
Nice to have
• Perhaps an open book suggesting the Bible, but not necessary.
Should not have
• No microphones or airwaves.

```html
<!DOCTYPE html>
<html lang="en">
<head>
<meta charset="utf-8">
<title>Morning Lanterns Over Hills — Podcast Cover Options</title>
<link rel="stylesheet" href="https://fonts.googleapis.com/css2?family=Anton&family=Permanent+Marker&display=swap">
<style>
  :root {
    --page: #ffffff;
    --amber: #b96f1f;
    --amber-deep: #a9601a;
    --stone: #6d6a66;
    --ink: #0b0b0b;
    --charcoal: #2b2b2b;
    --white: #ffffff;
    --orange: #f28c22;
    --yellow: #ffff00;
    --rule-dark: #3a1d08;
  }
  html, body {
    margin: 0;
    padding: 0;
    width: 1200px;
    height: 1079px;
    overflow: hidden;
    background: var(--page);
  }
  .board { display: block; width: 1200px; height: 1079px; }
  .title-block { font-family: "Anton", "Impact", sans-serif; }
  .title-script { font-family: "Permanent Marker", cursive; }
  .tag-word { font-family: "Anton", "Impact", sans-serif; }
</style>
</head>
<body>
<svg class="board" viewBox="0 0 1200 1079" xmlns="http://www.w3.org/2000/svg" role="group" aria-label="Four podcast cover options with small previews">
  <defs>
    <linearGradient id="photo-warm" x1="0" y1="0" x2="1" y2="1">
      <stop offset="0" stop-color="#5e5a55"/>
      <stop offset="0.3" stop-color="#3a3430"/>
      <stop offset="0.55" stop-color="#9a5a1c"/>
      <stop offset="1" stop-color="#b96f1f"/>
    </linearGradient>
    <radialGradient id="warm-glow" cx="1" cy="0" r="1">
      <stop offset="0" stop-color="#c27522"/>
      <stop offset="1" stop-color="#c27522" stop-opacity="0"/>
    </radialGradient>
    <linearGradient id="photo-dark" x1="0" y1="0" x2="1" y2="1">
      <stop offset="0" stop-color="#6a6865"/>
      <stop offset="0.3" stop-color="#2d2d2d"/>
      <stop offset="0.6" stop-color="#111111"/>
      <stop offset="1" stop-color="#050505"/>
    </linearGradient>
    <linearGradient id="hand-tone" x1="0" y1="0" x2="0" y2="1">
      <stop offset="0" stop-color="#d9d4cf" stop-opacity="0.55"/>
      <stop offset="1" stop-color="#d9d4cf" stop-opacity="0"/>
    </linearGradient>
    <filter id="lift" x="-10%" y="-10%" width="130%" height="130%">
      <feDropShadow dx="6" dy="8" stdDeviation="7" flood-color="#000" flood-opacity="0.55"/>
    </filter>

    <!-- Option A: amber, white title, brush tagline -->
    <symbol id="cover-amber-brush" viewBox="0 0 737 737">
      <g role="img" aria-label="Photo of a hand holding a black Holy Bible, toned amber">
        <rect width="737" height="737" fill="url(#photo-warm)"/>
        <rect width="737" height="737" fill="url(#warm-glow)"/>
        <path d="M175 320 q30 -20 60 0 l40 260 q-20 120 -60 157 h-60 q-30 -140 -10 -260 z" fill="url(#hand-tone)"/>
      </g>
      <rect x="140" y="212" width="122" height="48" fill="var(--white)"/>
      <text class="tag-word" x="201" y="251" font-size="40" text-anchor="middle" fill="var(--ink)">MORNING</text>
      <g class="title-block" fill="var(--white)" filter="url(#lift)">
        <text x="685" y="310" font-size="200" text-anchor="end" textLength="420" lengthAdjust="spacingAndGlyphs">LANTERNS</text>
        <text x="685" y="470" font-size="190" text-anchor="end" textLength="367" lengthAdjust="spacingAndGlyphs">OVER</text>
      </g>
      <text class="title-script" x="695" y="640" font-size="150" text-anchor="end" textLength="390" lengthAdjust="spacingAndGlyphs" fill="var(--yellow)" filter="url(#lift)">Hills</text>
    </symbol>

    <!-- Option B: amber, white title, ruled tagline -->
    <symbol id="cover-amber-ruled" viewBox="0 0 737 737">
      <g role="img" aria-label="Photo of a hand holding a black Holy Bible, toned amber">
        <rect width="737" height="737" fill="url(#photo-warm)"/>
        <rect width="737" height="737" fill="url(#warm-glow)"/>
        <path d="M175 320 q30 -20 60 0 l40 260 q-20 120 -60 157 h-60 q-30 -140 -10 -260 z" fill="url(#hand-tone)"/>
      </g>
      <rect x="140" y="212" width="122" height="48" fill="var(--white)"/>
      <text class="tag-word" x="201" y="251" font-size="40" text-anchor="middle" fill="var(--ink)">MORNING</text>
      <g class="title-block" fill="var(--white)" filter="url(#lift)">
        <text x="685" y="310" font-size="200" text-anchor="end" textLength="420" lengthAdjust="spacingAndGlyphs">LANTERNS</text>
        <text x="685" y="470" font-size="190" text-anchor="end" textLength="367" lengthAdjust="spacingAndGlyphs">OVER</text>
        <text x="693" y="630" font-size="150" text-anchor="end" textLength="320" lengthAdjust="spacingAndGlyphs">HILLS</text>
      </g>
      <rect x="314" y="494" width="380" height="6" fill="var(--rule-dark)"/>
      <rect x="314" y="649" width="380" height="6" fill="var(--rule-dark)"/>
    </symbol>

    <!-- Option C: dark, orange title, brush tagline -->
    <symbol id="cover-dark-brush" viewBox="0 0 737 737">
      <g role="img" aria-label="Black and white photo of a hand holding a black Holy Bible">
        <rect width="737" height="737" fill="url(#photo-dark)"/>
        <path d="M175 320 q30 -20 60 0 l40 260 q-20 120 -60 157 h-60 q-30 -140 -10 -260 z" fill="url(#hand-tone)"/>
      </g>
      <rect x="140" y="212" width="122" height="48" fill="var(--yellow)"/>
      <text class="tag-word" x="201" y="251" font-size="40" text-anchor="middle" fill="var(--ink)">MORNING</text>
      <g class="title-block" fill="var(--orange)" filter="url(#lift)">
        <text x="685" y="310" font-size="200" text-anchor="end" textLength="420" lengthAdjust="spacingAndGlyphs">LANTERNS</text>
        <text x="685" y="470" font-size="190" text-anchor="end" textLength="367" lengthAdjust="spacingAndGlyphs">OVER</text>
      </g>
      <text class="title-script" x="695" y="640" font-size="150" text-anchor="end" textLength="390" lengthAdjust="spacingAndGlyphs" fill="var(--yellow)" filter="url(#lift)">Hills</text>
    </symbol>

    <!-- Option D: dark, orange title, ruled tagline -->
    <symbol id="cover-dark-ruled" viewBox="0 0 737 737">
      <g role="img" aria-label="Black and white photo of a hand holding a black Holy Bible">
        <rect width="737" height="737" fill="url(#photo-dark)"/>
        <path d="M175 320 q30 -20 60 0 l40 260 q-20 120 -60 157 h-60 q-30 -140 -10 -260 z" fill="url(#hand-tone)"/>
      </g>
      <rect x="140" y="212" width="122" height="48" fill="var(--white)"/>
      <text class="tag-word" x="201" y="251" font-size="40" text-anchor="middle" fill="var(--ink)">MORNING</text>
      <g class="title-block" filter="url(#lift)">
        <text x="685" y="310" font-size="200" text-anchor="end" textLength="420" lengthAdjust="spacingAndGlyphs" fill="var(--orange)">LANTERNS</text>
        <text x="685" y="470" font-size="190" text-anchor="end" textLength="367" lengthAdjust="spacingAndGlyphs" fill="var(--orange)">OVER</text>
        <text x="693" y="630" font-size="150" text-anchor="end" textLength="320" lengthAdjust="spacingAndGlyphs" fill="var(--white)">HILLS</text>
      </g>
      <rect x="314" y="494" width="380" height="6" fill="var(--orange)"/>
      <rect x="314" y="649" width="380" height="6" fill="var(--orange)"/>
    </symbol>
  </defs>

  <g class="option option-a">
    <use href="#cover-amber-brush" x="38" y="62" width="436" height="436"/>
    <use href="#cover-amber-brush" x="501" y="432" width="66" height="66"/>
  </g>
  <g class="option option-b">
    <use href="#cover-amber-ruled" x="619" y="62" width="436" height="436"/>
    <use href="#cover-amber-ruled" x="1079" y="432" width="66" height="66"/>
  </g>
  <g class="option option-c">
    <use href="#cover-dark-brush" x="38" y="585" width="436" height="436"/>
    <use href="#cover-dark-brush" x="508" y="955" width="66" height="66"/>
  </g>
  <g class="option option-d">
    <use href="#cover-dark-ruled" x="619" y="585" width="436" height="436"/>
    <use href="#cover-dark-ruled" x="1081" y="955" width="66" height="66"/>
  </g>
</svg>
</body>
</html>
```